Poster for company's 5 NORMS

Good Day,

My name is Rilo and I am working for Karvell & Brodick Maritime Pte Ltd. We are in the Marine and Offshore industry and based in Singapore.

I have to submit a few A-2 sized poster design samples reflecting our 5 norms to my boss in 40 hours time. So I need your help.

The 5 norms are: (1) Ownership, (2) Positive Mindset, (3) Actions, (4) Teamwork, (5) Honesty.

My company logo can be googled. The corporate colours of the company are blue and grey predominantly and white is occasionally used. But feel free to play with colours. No need to stick to grey, blue and white. The words and headers, you can play with colours too. This poster must be an attention grabber. You can make it look professional yet fun as well.

A few of the poster designs should be build based on the following:
a) 2 liner headers reading the following:
Line 1: Our Winning 5 Norms!
LIne 2: OWNing the P.A.T.H to Tier 1

b) Bottom centre - company's logo

c) Design 1: A winding road (limit to 2 turns) as background and the 5 norms spread vertically along the winding road.

d) Design 2: A circle divided into 5 equal segments and in each segment, the 5 norms.

You should consider highlighting for the initial letter (s) of each word (OWN, P, A, T, H) so that it will reemphasize Owning the Path. Also, attached is a design for the poster that we have on our walls now. I did not scan it properly but I would want a much much better poster.

Please feel free to be creative, especially for the other designs.

Thank you very much. Looking forward to see posters in my inbox.

Have a great day ahead,

Regards, Rilo

Hp: 65-91357248

Good Day,

I just attached a picture of our current poster. I did not scan it well, apologies for that. But we would want a much much better poster.

Thank you!

Hello guys,

I have attached a picture of the company's logo. You can also visit the link below to get the correct logo.

It should state "Karvell & Brodick Maritime".

Thanks.

https://www.searchbox-example.sg/find?q=karvell+and+brodick+maritime+logo

Target Market(s)

Internal stakeholders. Good if it can impress clients as well.

Industry/Entity Type

Industry

Font styles to use
Serif

```html
<!DOCTYPE html>
<html lang="en">
<head>
<meta charset="utf-8">
<title>Our Winning 5 Norms — OWNing the P.A.T.H. to Tier I — Karvell &amp; Brodick Maritime</title>
<link rel="stylesheet" href="https://fonts.googleapis.com/css2?family=Playfair+Display:wght@400;700&display=swap">
<style>
  :root {
    --bg-light: #b2b2b2;
    --bg-mid: #a2a2a2;
    --bg-dark: #909090;
    --ink: #1d1d1d;
    --accent: #1d4f8f;
    --accent-light: #8cc0f2;
    --disc: rgba(40, 40, 40, 0.8);
    --disc-lead: rgba(30, 30, 30, 0.88);
    --label: #f0f0f0;
    --hands: rgba(18, 18, 18, 0.4);
    --mark: #2a2a2a;
  }
  * { margin: 0; padding: 0; box-sizing: border-box; }
  html, body { width: 848px; height: 1200px; overflow: hidden; }
  body { font-family: "Playfair Display", serif; }

  .poster {
    position: relative;
    width: 848px;
    height: 1200px;
    overflow: hidden;
    background: radial-gradient(ellipse at 50% 40%, var(--bg-light) 0%, var(--bg-mid) 60%, var(--bg-dark) 100%);
  }

  .headline {
    position: absolute;
    top: 18px;
    left: 0;
    width: 100%;
    text-align: center;
    color: var(--ink);
    font-weight: 400;
  }
  .headline__intro {
    display: block;
    font-size: 34px;
    line-height: 46px;
    letter-spacing: 3px;
    font-weight: 700;
  }
  .headline__line {
    display: block;
    font-size: 58px;
    line-height: 76px;
    letter-spacing: 2px;
  }
  .initial { color: var(--accent); font-weight: 700; }

  .norms-wheel {
    position: absolute;
    left: 0;
    top: 0;
    width: 848px;
    height: 1200px;
  }
  .norm-disc { fill: var(--disc); }
  .norm-disc--lead { fill: var(--disc-lead); }
  .norm-label {
    fill: var(--label);
    font-family: "Playfair Display", serif;
    font-size: 27px;
    letter-spacing: 2px;
  }
  .norm-label--small { font-size: 21px; letter-spacing: 1px; }
  .norm-label--wide { letter-spacing: 8px; }
  .norm-initial { fill: var(--accent-light); font-weight: 700; }

  .brand__dot {
    position: absolute;
    left: 206px;
    top: 1010px;
    width: 166px;
    height: 166px;
    border-radius: 50%;
    background: var(--mark);
  }
  .brand__name {
    position: absolute;
    left: 397px;
    top: 1072px;
    font-family: "Playfair Display", serif;
    font-size: 30px;
    line-height: 40px;
    letter-spacing: 1px;
    color: var(--mark);
  }
</style>
</head>
<body>
<main class="poster">
  <h1 class="headline">
    <span class="headline__intro">Our Winning 5 Norms!</span>
    <span class="headline__line"><span class="initial">OWN</span>ing the <span class="initial">P</span>.<span class="initial">A</span>.<span class="initial">T</span>.<span class="initial">H</span>.</span>
    <span class="headline__line">to Tier I</span>
  </h1>

  <svg class="norms-wheel" viewBox="0 0 636 900" aria-label="The five norms">
    <defs>
      <path id="ring-ownership" d="M319 449 A105 105 0 0 1 319 239 A105 105 0 0 1 319 449"/>
      <path id="ring-action" d="M381 408 A105 105 0 0 1 591 408 A105 105 0 0 1 381 408"/>
      <path id="ring-honesty" d="M379.8 531.8 A105 105 0 0 1 528.2 680.2 A105 105 0 0 1 379.8 531.8"/>
      <path id="ring-teamwork" d="M276.2 525 A105 105 0 0 1 155.8 697 A105 105 0 0 1 276.2 525"/>
      <path id="ring-mindset" d="M229.2 484.2 A105 105 0 0 1 80.8 335.8 A105 105 0 0 1 229.2 484.2"/>
    </defs>

    <g class="norm-discs">
      <circle class="norm-disc" cx="155" cy="410" r="136"/>
      <circle class="norm-disc" cx="216" cy="611" r="136"/>
      <circle class="norm-disc" cx="454" cy="606" r="136"/>
      <circle class="norm-disc" cx="486" cy="408" r="136"/>
      <circle class="norm-disc norm-disc--lead" cx="319" cy="344" r="136"/>
    </g>

    <circle class="hands-area" cx="318" cy="462" r="96" fill="var(--hands)" role="img"
            aria-label="Five hand silhouettes reaching toward the centre, one from each norm circle"/>

    <g class="norm-labels">
      <text class="norm-label"><textPath href="#ring-ownership" startOffset="50%" text-anchor="middle"><tspan class="norm-initial">Own</tspan>ership</textPath></text>
      <text class="norm-label norm-label--wide"><textPath href="#ring-action" startOffset="50%" text-anchor="middle"><tspan class="norm-initial">A</tspan>ction</textPath></text>
      <text class="norm-label"><textPath href="#ring-honesty" startOffset="50%" text-anchor="middle"><tspan class="norm-initial">H</tspan>onesty</textPath></text>
      <text class="norm-label"><textPath href="#ring-teamwork" startOffset="50%" text-anchor="middle"><tspan class="norm-initial">T</tspan>eamwork</textPath></text>
      <text class="norm-label norm-label--small"><textPath href="#ring-mindset" startOffset="50%" text-anchor="middle"><tspan class="norm-initial">P</tspan>ositive Mindset</textPath></text>
    </g>
  </svg>

  <footer class="brand">
    <span class="brand__dot" aria-hidden="true"></span>
    <p class="brand__name">Karvell &amp; Brodick<br>Maritime</p>
  </footer>
</main>
</body>
</html>
```